Boutique personal training and fitness studio - banner ad design

We need a 'revolving' banner ad designed for our personal training and fitness studio. There are three separate offers (i.e. 3 pages to the advertisements)
Offer 1
PT Starter Pack
3 personal training sessions
$119
New clients only
Offer 2
Group fitness
2 weeks unlimited group fitness classes
$29
New clients only
Offer 3
Strength starter pack
2 weeks unlimited group fitness classes and 2 PT sessions
$89
New clients only
Please do not put the words "Offer 1, 2 or 3" in the ads - just the text following each offer.
Each advertisement should be sized to fit across around half of the webpage and be in landscape format.
Each advertisement should have a suitable picture (no cartoons) and should be complimentary to the existing website.
Each advertisement should also include the logo (attached)
www.corrabankliftworks.com.au
Training

```html
<!DOCTYPE html>
<html lang="en">
<head>
<meta charset="utf-8">
<title>PT Starter Pack – Corrabank Liftworks</title>
<link rel="stylesheet" href="https://fonts.googleapis.com/css2?family=Oswald:wght@500;600&family=Roboto:wght@400;500;700&display=swap">
<style>
  :root {
    --brand-red: #c8202a;
    --deep-red: #8c161c;
    --ink: #1b1b1b;
    --slate: #3b3b3b;
    --band-dark: #141414;
    --band-mid: #3a3a3a;
    --paper: #ffffff;
    --mat-blue: #2f63a8;
    --mat-light: #7fa9d8;
  }
  * { margin: 0; padding: 0; box-sizing: border-box; }
  html, body { width: 1200px; height: 599px; overflow: hidden; background: var(--paper); }
  .banner {
    position: relative;
    width: 1200px;
    height: 599px;
    overflow: hidden;
    background: var(--paper);
    font-family: "Roboto", Arial, sans-serif;
  }
  .banner__shapes { position: absolute; inset: 0; }
  .brand {
    position: absolute;
    left: 26px;
    top: 58px;
    display: flex;
    align-items: center;
    gap: 14px;
  }
  .brand__mark { width: 22px; height: 22px; background: var(--brand-red); }
  .brand__name {
    font-family: "Oswald", "Arial Narrow", sans-serif;
    font-weight: 600;
    font-size: 34px;
    letter-spacing: 1px;
    text-transform: uppercase;
    color: var(--paper);
    line-height: 1;
  }
  .offer__title,
  .offer__count,
  .offer__line {
    position: absolute;
    font-weight: 500;
    line-height: 1;
    white-space: nowrap;
  }
  .offer__title {
    left: 38px;
    top: 290px;
    font-size: 50px;
    color: var(--brand-red);
  }
  .offer__count {
    left: 36px;
    top: 360px;
    font-size: 100px;
    color: var(--brand-red);
  }
  .offer__line {
    left: 106px;
    font-size: 46px;
    color: var(--slate);
  }
  .offer__line--first { top: 396px; }
  .offer__line--second { top: 452px; }
  .cta {
    position: absolute;
    left: 387px;
    top: 456px;
  }
  .cta__note {
    font-weight: 700;
    font-size: 27px;
    color: var(--ink);
    margin-left: 74px;
    margin-bottom: 6px;
    white-space: nowrap;
  }
  .cta__row { display: flex; height: 88px; gap: 4px; }
  .cta__price, .cta__action {
    display: flex;
    align-items: center;
    justify-content: center;
    font-family: "Oswald", "Arial Narrow", sans-serif;
    color: var(--paper);
    border: 3px solid var(--paper);
    outline: 2px solid var(--deep-red);
  }
  .cta__price {
    width: 168px;
    background: var(--brand-red);
    font-size: 66px;
    font-weight: 500;
  }
  .cta__action {
    width: 232px;
    background: var(--deep-red);
    font-size: 44px;
    font-weight: 600;
    text-transform: uppercase;
  }
</style>
</head>
<body>
<main class="banner">
  <svg class="banner__shapes" width="1200" height="599" viewBox="0 0 1200 599">
    <defs>
      <linearGradient id="band-fill" x1="0" y1="0" x2="1" y2="1">
        <stop offset="0" stop-color="var(--band-mid)"/>
        <stop offset="0.6" stop-color="var(--band-dark)"/>
      </linearGradient>
      <linearGradient id="photo-fill" x1="0" y1="0" x2="1" y2="1">
        <stop offset="0" stop-color="#1d2a3c"/>
        <stop offset="0.35" stop-color="var(--mat-blue)"/>
        <stop offset="0.7" stop-color="var(--mat-light)"/>
        <stop offset="1" stop-color="#4f7fbf"/>
      </linearGradient>
    </defs>
    <path class="photo-area" role="img" aria-label="Personal trainer guiding a client through sit-ups on a blue gym mat"
          fill="url(#photo-fill)"
          d="M300 0 H1200 V590 C900 400 500 230 0 205 V175 C160 150 250 90 300 0 Z"/>
    <path class="brand-band" fill="url(#band-fill)"
          d="M0 0 H560 C470 70 360 150 0 200 Z"/>
    <path class="accent-curve" fill="none" stroke="var(--brand-red)" stroke-width="5"
          d="M0 205 C500 230 900 400 1200 590"/>
  </svg>

  <div class="brand">
    <span class="brand__mark"></span>
    <span class="brand__name">Corrabank Liftworks</span>
  </div>

  <section class="offer">
    <h1 class="offer__title">PT Starter Pack</h1>
    <span class="offer__count">3</span>
    <p class="offer__line offer__line--first">Personal Training</p>
    <p class="offer__line offer__line--second">Sessions</p>
  </section>

  <div class="cta">
    <p class="cta__note">New Clients Only</p>
    <div class="cta__row">
      <span class="cta__price">$119</span>
      <span class="cta__action">Book Now</span>
    </div>
  </div>
</main>
</body>
</html>
```